Pelin Thai Massage Double Sided Flyer Luxury

I require a double sided flyer
we are a Thai Massage Spa
Would like gold, deep purple and bronze colours
Something eye catching and looks professional

```html
<!DOCTYPE html>
<html lang="en">
<head>
<meta charset="utf-8">
<title>Pelin Thai Massage – Double Sided Flyer</title>
<link rel="stylesheet" href="https://fonts.googleapis.com/css2?family=Philosopher&family=Tinos:wght@400;700&family=Roboto:wght@400;500;700&display=swap">
<style>
  :root{
    --bg:#2c2c2c;
    --purple-deep:#3b145f;
    --purple:#6a23b0;
    --purple-bright:#9a3fd0;
    --indigo:#2c3a91;
    --gold:#f0c23a;
    --gold-dark:#c98f22;
    --bronze:#d9902a;
    --white:#ffffff;
    --text-purple:#5a2a9a;
  }
  *{box-sizing:border-box;margin:0;padding:0}
  html,body{width:936px;height:1200px;overflow:hidden;background:var(--bg)}
  .flyer-side{position:absolute;left:116px;width:704px;background:var(--white);overflow:hidden}
  .flyer-front{top:90px;height:492px}
  .flyer-back{top:632px;height:488px}

  /* front */
  .front-field{position:absolute;left:0;top:0;width:100%;height:430px;
    background:linear-gradient(160deg,var(--purple) 0%,var(--purple-bright) 45%,var(--indigo) 100%)}
  .front-frame{position:absolute;left:18px;top:21px;width:654px;height:237px;border:2px solid var(--gold)}
  .brand{position:absolute;text-align:center;font-family:"Philosopher",sans-serif;color:var(--gold)}
  .brand-mark{display:block;margin:0 auto;border-radius:50%;border:3px solid var(--gold)}
  .brand-name{font-size:26px;white-space:nowrap}
  .front-brand{left:37px;top:58px;width:231px}
  .front-brand .brand-mark{width:110px;height:110px;margin-bottom:10px}
  .intro{position:absolute;left:301px;top:44px;width:348px;font-family:"Tinos",serif;
    font-size:16px;line-height:20px;color:var(--white);text-align:justify}
  .intro p+p{margin-top:14px}
  .intro strong{color:var(--gold);font-weight:700}
  .tagline-box{position:absolute;left:23px;top:270px;width:645px;height:55px;background:var(--white);
    border-radius:28px;box-shadow:0 0 0 3px var(--purple-deep);display:flex;align-items:center;justify-content:center;
    padding:4px 80px 0;font-family:"Tinos",serif;font-size:15px;line-height:20px;color:var(--text-purple);text-align:center}
  .section-pill{position:absolute;font-family:"Philosopher",sans-serif;display:flex;align-items:center;justify-content:center}
  .front-pill{left:253px;top:250px;width:185px;height:30px;border-radius:7px;font-size:21px;color:var(--purple-deep);
    background:linear-gradient(90deg,var(--gold-dark),var(--gold) 45%,#ffe27a 60%,var(--gold-dark))}
  .perk{position:absolute;font-family:"Tinos",serif;font-weight:700;font-size:16.5px;color:var(--white);white-space:nowrap}
  .perk-open{left:75px;top:366px}
  .perk-gift{left:376px;top:339px;display:flex;align-items:center}
  .gift-box{width:53px;height:53px;background:var(--purple-deep);display:flex;align-items:flex-end;justify-content:center;
    padding-bottom:8px;font-size:16.5px;margin-right:4px;border-top:6px solid var(--purple)}
  .call-pill{position:absolute;font-family:"Roboto",sans-serif;font-weight:700;color:var(--gold);background:var(--purple-deep);
    display:flex;align-items:center;justify-content:center;white-space:nowrap}
  .front-call{left:179px;top:408px;width:292px;height:41px;border-radius:21px;font-size:22px}
  .contact{position:absolute;display:flex;align-items:center;font-family:"Roboto",sans-serif;font-size:15px;color:var(--text-purple);white-space:nowrap}
  .contact svg{width:20px;height:20px;margin-right:10px;flex:none}
  .front-address{left:82px;top:460px}
  .front-web{left:370px;top:460px}

  /* back */
  .back-frame{position:absolute;left:23px;top:41px;width:647px;height:426px;border:2px solid var(--gold)}
  .back-disc{position:absolute;left:0;top:0}
  .back-brand{left:40px;top:52px;width:240px}
  .back-brand .brand-mark{width:120px;height:120px;margin-bottom:16px}
  .back-pill{left:389px;top:71px;width:210px;height:28px;border-radius:0 14px 14px 0;justify-content:flex-start;padding-left:12px;
    font-size:21px;color:var(--white);background:linear-gradient(90deg,var(--purple),var(--purple-bright))}
  .price-list{position:absolute;left:398px;top:120px;list-style:none;font-family:"Roboto",sans-serif}
  .price-list li{position:relative;padding-left:16px;margin-bottom:18px}
  .price-list li::before{content:"";position:absolute;left:0;top:6px;width:4px;height:4px;border-radius:50%;background:var(--text-purple)}
  .price-title{font-weight:700;font-size:13.5px;color:var(--text-purple);display:block}
  .price-note{font-size:12.5px;line-height:16px;color:var(--bronze);display:block;margin-top:2px}
  .back-address{left:40px;top:392px;font-weight:700;font-size:14px}
  .back-web{left:40px;top:427px;font-weight:700;font-size:14px}
  .back-call{left:293px;top:391px;width:411px;height:53px;border-radius:26px 0 0 26px;font-size:25px;justify-content:flex-start;padding-left:24px}
  .back-call svg{width:28px;height:28px;margin-right:20px}
</style>
</head>
<body>

<section class="flyer-side flyer-front" aria-label="Flyer front">
  <div class="front-field"></div>
  <div class="front-frame"></div>

  <div class="brand front-brand">
    <span class="brand-mark"></span>
    <span class="brand-name">Pelin Thai Massage</span>
  </div>

  <div class="intro">
    <p>Set in the heart of Roundhay, <strong>Pelin Thai Massage</strong> will allow you to immerse yourself in a place where your wellbeing and rejuvenation is at the centre of what we do.</p>
    <p>Using Thai traditions, our highly trained therapists offer revitalising body treatments with their deep tissue massage techniques. In their hands, you will see and feel immediate results.</p>
  </div>

  <div class="tagline-box">Restore balance. Revive your senses. Discover all the ways Pelin Thai Massage can breathe new life into your body and soul.</div>
  <div class="section-pill front-pill">Massages</div>

  <div class="perk perk-open">OPEN 7 DAYS A WEEK</div>
  <div class="perk perk-gift"><span class="gift-box">GIFT</span>VOUCHERS AVAILABLE</div>

  <div class="call-pill front-call">CALL NOW 0113 496 0712</div>

  <div class="contact front-address">
    <svg viewBox="0 0 20 20" aria-hidden="true"><circle cx="10" cy="10" r="10" fill="#7a3bbf"/><path d="M5 10 L10 5.5 L15 10 V15 H5 Z" fill="#fff"/><rect x="8.5" y="11" width="3" height="4" fill="#7a3bbf"/></svg>
    42 Willow Row, Leeds, LS8 4QT
  </div>
  <div class="contact front-web">
    <svg viewBox="0 0 20 20" aria-hidden="true"><circle cx="10" cy="10" r="10" fill="#7a3bbf"/><g fill="none" stroke="#fff" stroke-width="1.2"><circle cx="10" cy="10" r="5.5"/><ellipse cx="10" cy="10" rx="2.3" ry="5.5"/><path d="M4.5 10 H15.5"/></g></svg>
    www.pelinthaimassage.co.uk
  </div>
</section>

<section class="flyer-side flyer-back" aria-label="Flyer back">
  <div class="back-frame"></div>
  <svg class="back-disc" width="704" height="488" viewBox="0 0 704 488" aria-hidden="true">
    <defs>
      <linearGradient id="discFill" x1="0" y1="0" x2="1" y2="1">
        <stop offset="0" stop-color="#5d1fa3"/>
        <stop offset="0.5" stop-color="#8a33c6"/>
        <stop offset="1" stop-color="#3a3a9a"/>
      </linearGradient>
    </defs>
    <circle cx="148" cy="114" r="224" fill="#4a1a85"/>
    <circle cx="144" cy="104" r="222" fill="#ffffff"/>
    <circle cx="140" cy="100" r="218" fill="url(#discFill)"/>
  </svg>

  <div class="brand back-brand">
    <span class="brand-mark"></span>
    <span class="brand-name">Pelin Thai Massage</span>
  </div>

  <div class="section-pill back-pill">Massages</div>
  <ul class="price-list">
    <li><span class="price-title">DEEP TISSUE MASSAGE</span></li>
    <li><span class="price-title">60 minutes £45</span><span class="price-note">Oil massage personalised,<br>light to firm pressure</span></li>
    <li><span class="price-title">90 minutes £55</span><span class="price-note">Oil massage, medium to firm pressure</span></li>
    <li><span class="price-title">THAI FLOOR TRADTIONAL MASSAGE</span></li>
    <li><span class="price-title">60 MINUTES £45</span><span class="price-note">Dry massage, medium to firm pressure<br>applying stretching technique</span></li>
  </ul>

  <div class="contact back-address">
    <svg viewBox="0 0 20 20" aria-hidden="true"><circle cx="10" cy="10" r="10" fill="#7a3bbf"/><path d="M5 10 L10 5.5 L15 10 V15 H5 Z" fill="#fff"/><rect x="8.5" y="11" width="3" height="4" fill="#7a3bbf"/></svg>
    42 Willow Row, Leeds, LS8 4QT
  </div>
  <div class="contact back-web">
    <svg viewBox="0 0 20 20" aria-hidden="true"><circle cx="10" cy="10" r="10" fill="#7a3bbf"/><g fill="none" stroke="#fff" stroke-width="1.2"><circle cx="10" cy="10" r="5.5"/><ellipse cx="10" cy="10" rx="2.3" ry="5.5"/><path d="M4.5 10 H15.5"/></g></svg>
    www.pelinthaimassage.co.uk
  </div>

  <div class="call-pill back-call">
    <svg viewBox="0 0 24 24" aria-hidden="true"><path fill="#ffffff" d="M6.6 10.8a15.1 15.1 0 0 0 6.6 6.6l2.2-2.2a1 1 0 0 1 1-.25 11.4 11.4 0 0 0 3.6.57 1 1 0 0 1 1 1V20a1 1 0 0 1-1 1A17 17 0 0 1 3 4a1 1 0 0 1 1-1h3.5a1 1 0 0 1 1 1c0 1.25.2 2.45.57 3.6a1 1 0 0 1-.25 1z"/></svg>
    CALL NOW 0113 496 0712
  </div>
</section>

</body>
</html>
```